Business card for Chicago based Private Equity Company

We need a business card for our PE company called Crestline Partners. We want a simple and clean, yet creative card design. The back side should reflect our logo. Also would like to see embossed ideas. Should reflect strength and growth. Our logo is attached. Also need editable file. Details are as follows for Business Card:

Dale Moravec Co-Founder 2750 Larkin Avenue Suite 410 Oak Brook, IL 60587 http://www.crestlinepartnersllc.example (D) 630.555.0142 (C) 312.555.0178 (E) dm@crestlinepartnersllc.example

```html
<!DOCTYPE html>
<html lang="en">
<head>
<meta charset="utf-8">
<title>Crestline Partners – Business Card</title>
<link rel="stylesheet" href="https://fonts.googleapis.com/css2?family=Lato:wght@400;700&display=swap">
<style>
  :root {
    --backdrop: #3b3b3d;
    --card: #161617;
    --card-deep: #0b0b0c;
    --ink: #f2f2f2;
    --ink-soft: #d9d9d9;
    --watermark: #1d1d1f;
  }
  * { box-sizing: border-box; margin: 0; padding: 0; }
  html, body {
    width: 1200px; height: 926px; overflow: hidden;
    background: var(--backdrop);
    font-family: "Lato", Arial, sans-serif;
  }
  .sheet {
    position: relative; width: 1200px; height: 926px;
    display: flex; flex-direction: column; align-items: center; justify-content: center; gap: 42px;
  }
  .card {
    position: relative; width: 700px; height: 400px;
    background: var(--card); overflow: hidden;
    box-shadow: 0 10px 30px rgba(0,0,0,.35);
  }

  /* Back side: embossed wordmark */
  .card--back { display: flex; align-items: center; justify-content: center; }
  .emboss {
    display: flex; align-items: center; gap: 18px;
    color: var(--card-deep);
  }
  .emboss__disc { flex: none; width: 70px; height: 70px; border-radius: 50%; background: var(--card-deep); }
  .emboss__name {
    font-weight: 400; font-size: 34px; letter-spacing: 4px; line-height: 1.1;
    text-transform: uppercase; white-space: nowrap;
  }

  /* Front side */
  .watermark {
    position: absolute; left: 300px; top: 40px;
    width: 360px; height: 360px; border-radius: 50%;
    border: 46px solid var(--watermark);
  }
  .brand {
    position: absolute; left: 56px; top: 130px;
    display: flex; align-items: center; gap: 10px; color: var(--ink);
  }
  .brand__disc { flex: none; width: 30px; height: 30px; border-radius: 50%; background: var(--ink); }
  .brand__name {
    font-weight: 400; font-size: 14px; letter-spacing: 1.5px; text-transform: uppercase;
    line-height: 1.1; white-space: nowrap;
  }
  .address {
    position: absolute; left: 56px; top: 205px;
    font-style: normal; color: var(--ink-soft);
    font-size: 15px; line-height: 24px;
  }
  .person {
    position: absolute; left: 340px; top: 104px; color: var(--ink);
  }
  .person__name { font-size: 29px; font-weight: 400; letter-spacing: 1px; text-transform: uppercase; line-height: 1.2; white-space: nowrap; }
  .person__name strong { font-weight: 700; }
  .person__role { font-size: 16px; letter-spacing: 1px; text-transform: uppercase; color: var(--ink-soft); margin-top: 2px; }
  .contact {
    position: absolute; left: 340px; top: 206px; list-style: none;
    color: var(--ink-soft); font-size: 17px; line-height: 27px; white-space: nowrap;
  }
</style>
</head>
<body>
<main class="sheet">
  <section class="card card--back" aria-label="Card back">
    <div class="emboss">
      <span class="emboss__disc"></span>
      <span class="emboss__name">Crestline Partners</span>
    </div>
  </section>

  <section class="card card--front" aria-label="Card front">
    <div class="watermark"></div>
    <div class="brand">
      <span class="brand__disc"></span>
      <span class="brand__name">Crestline Partners</span>
    </div>
    <address class="address">
      2750 Larkin Avenue<br>
      Suite 410 Oak Brook, IL 60587
    </address>
    <div class="person">
      <h1 class="person__name">Dale <strong>Moravec</strong></h1>
      <p class="person__role">Co-Founder</p>
    </div>
    <ul class="contact">
      <li>(D) 630.555.0142</li>
      <li>(C) 312.555.0178</li>
      <li>(E) dm@crestlinepartnersllc.example</li>
      <li>http://www.crestlinepartnersllc.example</li>
    </ul>
  </section>
</main>
</body>
</html>
```